Voreta Okeru Fanvita

Design a self adhesive label to be placed on a standard 1 pint milk plastic bottle 14.acm x 5.5 cm and 1 litre plastic bottle 17cm X 6.1cm

The product to be packed inside the bottle is a Natural Fermented Milk which looks between Natural Yogurt but with curdle inside.
Updates

I have update project to a guaranteed contest

Target Market(s)

Small Ethnic African Community from Southern Africa

Industry/Entity Type

Plastic

Requirements
Must have
• Logo/Brand VORETA and Product Name which is a double word OKERU FANVITA.

```html
<!DOCTYPE html>
<html lang="en">
<head>
<meta charset="utf-8">
<title>Voreta Okeru Fanvita – Bottle Label</title>
<link rel="stylesheet" href="https://fonts.googleapis.com/css2?family=Roboto+Condensed:wght@300;700&family=Yellowtail&display=swap">
<style>
  :root {
    --red: #e8212b;
    --ink: #111111;
    --grey-text: #8a8a8a;
    --caption: #b5b5b5;
    --paper: #ffffff;
    --art-fill: #e9e9e9;
  }
  * { box-sizing: border-box; margin: 0; padding: 0; }
  html, body { width: 1200px; height: 900px; overflow: hidden; background: var(--paper); }
  .canvas { position: relative; width: 1200px; height: 900px; }

  .label {
    position: absolute; left: 94px; top: 209px; width: 1008px; height: 401px;
    background: var(--paper);
    border: 4px dashed var(--ink);
    box-shadow: 0 0 40px 6px rgba(0,0,0,0.12);
  }
  .divider {
    position: absolute; top: 22px; bottom: 22px; width: 0;
    border-left: 4px dashed var(--ink);
  }
  .divider--left { left: 176px; }
  .divider--right { left: 857px; }

  .brand-strip { position: absolute; left: 0; top: 0; width: 176px; height: 100%; }
  .brand-name {
    position: absolute; left: 46px; top: 26px; height: 340px;
    writing-mode: vertical-rl; transform: rotate(180deg);
    font-family: "Roboto Condensed", sans-serif; font-weight: 700;
    font-size: 84px; line-height: 72px; color: var(--red);
    text-align: center;
  }
  .product-type {
    position: absolute; left: 130px; top: 90px; height: 210px;
    writing-mode: vertical-rl; transform: rotate(180deg);
    font-family: "Roboto Condensed", sans-serif; font-weight: 300;
    font-size: 17px; color: var(--grey-text); text-align: center;
  }

  .artwork {
    position: absolute; left: 220px; top: 12px; width: 500px; height: 238px;
    background: var(--art-fill); border-radius: 6px;
  }
  .volume {
    position: absolute; left: 728px; top: 20px;
    font-family: "Yellowtail", cursive; font-size: 46px; color: var(--red);
  }
  .product-name {
    position: absolute; left: 240px; top: 250px; width: 580px;
    font-family: "Yellowtail", cursive; font-size: 92px; line-height: 1.1;
    color: var(--red); text-align: center; white-space: nowrap;
  }

  .info-panel { position: absolute; left: 876px; top: 22px; width: 112px; }
  .panel-heading {
    font-family: "Yellowtail", cursive; font-size: 19px; color: var(--ink);
    white-space: nowrap;
  }
  .info-box { height: 118px; margin: 4px 0 20px; }
  .nutrition {
    margin-top: 4px; border-top: 2px solid var(--ink);
    font-family: Arial, Helvetica, sans-serif; font-size: 5.5px; line-height: 8px; color: var(--ink);
  }
  .nutrition .row {
    display: flex; justify-content: space-between;
    border-bottom: 0.6px solid var(--ink);
  }
  .nutrition .row--thick { border-bottom-width: 2px; }
  .nutrition .indent { padding-left: 6px; }
  .nutrition b { font-weight: 700; }
  .nutrition .note { font-size: 4.5px; line-height: 6px; padding-top: 1px; }

  .caption-rule {
    position: absolute; left: 137px; top: 840px; width: 926px;
    border-top: 1px dashed #dcdcdc;
  }
  .caption {
    position: absolute; left: 0; top: 856px; width: 1200px; text-align: center;
    font-family: "Roboto Condensed", sans-serif; font-weight: 300;
    font-size: 16px; letter-spacing: 0.5px; color: var(--caption);
  }
</style>
</head>
<body>
<main class="canvas">
  <section class="label">
    <div class="brand-strip">
      <div class="brand-name">voreta</div>
      <div class="product-type">Full Cream Milk Powder</div>
    </div>
    <div class="divider divider--left"></div>

    <div class="artwork" role="img" aria-label="Hand-drawn black and white spotted cow surrounded by scattered black hearts"></div>
    <div class="volume">1 litre</div>
    <h1 class="product-name">Okeru Fanvita</h1>

    <div class="divider divider--right"></div>
    <aside class="info-panel">
      <div class="panel-heading">Additional Info</div>
      <div class="info-box"></div>
      <div class="panel-heading">Nutrition Facts</div>
      <div class="nutrition">
        <div class="row"><b>Amount Per Serving</b></div>
        <div class="row row--thick"><b>Calories 170</b><span>Calories from Fat 80</span></div>
        <div class="row" style="justify-content:flex-end"><b>% Daily Value*</b></div>
        <div class="row"><b>Total Fat 9g</b><span>14%</span></div>
        <div class="row indent"><span>Saturated Fat 5g</span><span>25%</span></div>
        <div class="row indent"><span>Trans Fat 0g</span></div>
        <div class="row"><b>Cholesterol 30mg</b><span>10%</span></div>
        <div class="row"><b>Sodium 125mg</b><span>5%</span></div>
        <div class="row"><b>Total Carbohydrate 13g</b><span>4%</span></div>
        <div class="row indent"><span>Dietary Fiber 0g</span><span>0%</span></div>
        <div class="row indent"><span>Sugars 12g</span></div>
        <div class="row row--thick"><b>Protein 8g</b></div>
        <div class="row"><span>Vitamin A 6%</span><span>Vitamin C 4%</span></div>
        <div class="row"><span>Calcium 30%</span><span>Iron 0%</span></div>
        <div class="note">*Percent Daily Values are based on a 2,000 calorie diet.</div>
      </div>
    </aside>
  </section>

  <div class="caption-rule"></div>
  <p class="caption">Label Okeru Fanvita - base version</p>
</main>
</body>
</html>
```